Clone http://www.velvorquillset.com/ (fully functioning WordPress website - not just design)

1) Clone or recreate http://www.velvorquillset.com/ in Wordpress with WooCommerece plugin
2) Connect to our Existing Quenz Account
3) Make site-wide text only changes that we provide you when site is complete.

We will provide all the graphics according to your size requirements.

Cash awarded to the closest copy of http://www.velvorquillset.com/

Target Market(s)

WordPress developer

Number of Pages Required

5+ page

Font styles to use
Sans Serif

Colors
abd037
cadf82
eaf2ce

Requirements
Must have
• Fully functioning website.

```html
<!DOCTYPE html>
<html lang="en">
<head>
<meta charset="utf-8">
<title>Cedar Crest Consulting</title>
<link rel="stylesheet" href="https://fonts.googleapis.com/css2?family=Jost:wght@400;500&family=Open+Sans:wght@400;600&display=swap">
<style>
:root{
  --green:#abd037;
  --green-mid:#cadf82;
  --green-pale:#eaf2ce;
  --ink:#1c1c1c;
  --heading-grey:#5f5f5f;
  --body-grey:#6c6c6c;
  --card-line:#cfcfcf;
  --footer-bg:#ececec;
  --bar-bg:#d8d8d8;
  --white:#ffffff;
}
*{margin:0;padding:0;box-sizing:border-box}
html,body{width:1200px;height:2579px;overflow:hidden;background:var(--white)}
body{position:relative;font-family:"Open Sans",Arial,sans-serif;color:var(--ink)}
.hero{position:absolute;left:0;top:0;width:1200px;height:663px;overflow:hidden}
.hero-photo{position:absolute;inset:0;background:
  radial-gradient(ellipse 420px 260px at 900px 330px,#2a2a2a 0%,rgba(40,40,40,.6) 45%,transparent 70%),
  linear-gradient(180deg,#6f5a48 0%,#8a6f52 30%,#7d8a3c 45%,#a9865d 62%,#b08a60 80%,#7a5c40 100%)}
.hero-shade{position:absolute;inset:0;background:linear-gradient(90deg,rgba(30,22,15,.55) 0%,rgba(30,22,15,.15) 55%,rgba(30,22,15,.05) 100%)}
.brand{position:absolute;left:137px;top:58px;display:flex;align-items:center;gap:14px;color:var(--white);font-family:"Jost",sans-serif;font-size:31px;font-weight:400}
.brand-dot{width:26px;height:26px;border-radius:50%;background:var(--white)}
.nav{position:absolute;top:60px;left:584px;display:flex;gap:36px;font-family:"Jost",sans-serif;font-size:18px;color:var(--white)}
.nav .active{color:var(--green)}
.hero-title{position:absolute;left:118px;top:222px;font-family:"Jost",sans-serif;font-size:46px;font-weight:400;line-height:56px;color:var(--white)}
.hero-title .accent{color:var(--green)}
.hero-text{position:absolute;left:118px;top:350px;width:460px;font-size:14px;line-height:24px;color:var(--white)}
.btn{display:block;background:var(--green);color:var(--white);font-family:"Jost",sans-serif;font-weight:500;text-align:center}
.hero-btn{position:absolute;left:118px;top:425px;width:195px;height:44px;line-height:44px;font-size:18px}
.dots{position:absolute;left:596px;top:622px;display:flex;gap:9px}
.dots span{width:15px;height:15px;border-radius:50%;background:var(--white)}
.dots .current{background:transparent;border:2px solid var(--white)}
.section-title{position:absolute;top:716px;width:1200px;text-align:center;font-family:"Jost",sans-serif;font-size:40px;font-weight:400;color:var(--heading-grey)}
.service{position:absolute;left:133px;width:943px;height:369px;border:2px solid var(--card-line);border-radius:14px;overflow:hidden;background:var(--white)}
.badge{position:absolute;top:0;width:100px;height:104px;background:var(--green);color:var(--white);font-family:"Jost",sans-serif;font-size:38px;display:flex;align-items:center;justify-content:center}
.badge.left{left:0;border-radius:0 0 100% 0;padding:0 14px 4px 0}
.badge.right{right:0;border-radius:0 0 0 100%;padding:0 0 4px 14px}
.service-copy{position:absolute;top:80px;width:410px}
.service-copy h2{font-family:"Jost",sans-serif;font-weight:400;font-size:30px;color:var(--ink);margin-bottom:14px}
.service-copy h3{font-size:16.5px;font-weight:400;color:var(--ink);margin-bottom:8px}
.service-copy p{font-size:12.5px;line-height:21px;color:var(--body-grey)}
.service-art{position:absolute;background:radial-gradient(circle at 50% 50%,var(--green-pale) 0%,var(--white) 72%);border-radius:8px}
.cta{position:absolute;left:490px;top:2038px;width:224px;height:46px;line-height:46px;font-size:17.5px}
.cta-note{position:absolute;top:2102px;width:1200px;text-align:center;font-size:13.5px;color:#8a8a8a}
.footer{position:absolute;left:0;top:2207px;width:1200px;height:303px;background:var(--footer-bg)}
.footer-brand{position:absolute;left:128px;top:95px;display:flex;align-items:center;gap:10px;font-family:"Jost",sans-serif;font-size:24px;color:var(--ink)}
.footer-brand span{width:22px;height:22px;border-radius:50%;background:var(--green)}
.footer-col{position:absolute;top:63px}
.footer-col h4{font-family:"Jost",sans-serif;font-weight:400;font-size:21px;color:var(--ink);margin-bottom:8px}
.footer-col li{list-style:none;font-size:13px;line-height:30px;color:var(--body-grey)}
.social{display:flex;gap:8px;margin-top:4px}
.social span{width:37px;height:37px;border-radius:50%;border:1.5px solid #555}
.bottom-bar{position:absolute;left:0;top:2510px;width:1200px;height:69px;background:var(--bar-bg);text-align:center;line-height:69px;font-size:12.5px;color:#333}
</style>
</head>
<body>
<header class="hero">
  <div class="hero-photo" role="img" aria-label="Photo of a bright office desk with a monitor, apple, notebook and green partition"></div>
  <div class="hero-shade"></div>
  <div class="brand"><span class="brand-dot"></span>Cedar Crest</div>
  <nav class="nav"><span class="active">Home</span><span>About Us</span><span>Services</span><span>Our Team</span><span>Contact</span></nav>
  <h1 class="hero-title"><span class="accent">Cedar Crest</span><br>Consulting Services</h1>
  <p class="hero-text">Praesent elementum elit at tellus nec ultricies sit amet porttitor mattis enim In massa libero interdum nec interduv</p>
  <a class="btn hero-btn">Learn More</a>
  <div class="dots"><span class="current"></span><span></span><span></span><span></span></div>
</header>

<h2 class="section-title">What Cedar Crest Provide</h2>

<section class="service" style="top:821px">
  <div class="badge left">01</div>
  <div class="service-copy" style="left:108px">
    <h2>Business Consulting</h2>
    <h3>Praesent elementum elit at tellus nec ultricies sit</h3>
    <p>amet porttitor mattis enim In massa libero interdum nec interdum vel blandit sed nulla In ullamcorper est eget tempor cursus neque mi consectetuer mi a ultricies massa est sed nisl Class aptent taciti sociosqu ad litora torquent per conubia nostra per inceptos hymenaeos Proin nulla arcu nonummy luctus dictum</p>
  </div>
  <div class="service-art" role="img" aria-label="Green line illustration of two consultants at a table with a speech bubble" style="left:602px;top:60px;width:250px;height:250px"></div>
</section>

<section class="service" style="top:1221px">
  <div class="badge right">02</div>
  <div class="service-art" role="img" aria-label="Green line illustration of a light bulb with a dollar sign" style="left:112px;top:34px;width:226px;height:282px"></div>
  <div class="service-copy" style="left:462px">
    <h2>Financial Consulting</h2>
    <h3>Praesent elementum elit at tellus nec ultricies sit</h3>
    <p>amet porttitor mattis enim In massa libero interdum nec interdum vel blandit sed nulla In ullamcorper est eget tempor cursus neque mi consectetuer mi a ultricies massa est sed nisl Class aptent taciti sociosqu ad litora torquent per conubia nostra per inceptos hymenaeos Proin nulla arcu nonummy luctus dictum</p>
  </div>
</section>

<section class="service" style="top:1621px">
  <div class="badge left">03</div>
  <div class="service-copy" style="left:114px">
    <h2>Grow Your Business</h2>
    <h3>Praesent elementum elit at tellus nec ultricies sit</h3>
    <p>amet porttitor mattis enim In massa libero interdum nec interdum vel blandit sed nulla In ullamcorper est eget tempor cursus neque mi consectetuer mi a ultricies massa est sed nisl Class aptent taciti sociosqu ad litora torquent per conubia nostra per inceptos hymenaeos Proin nulla arcu nonummy luctus dictum</p>
  </div>
  <div class="service-art" role="img" aria-label="Green line illustration of a hand holding a plant growing coins" style="left:600px;top:40px;width:226px;height:264px"></div>
</section>

<a class="btn cta">Get Started Now</a>
<p class="cta-note">Class aptent taciti sociosqu ad litora torquent per conubia nostra per inceptos</p>

<footer class="footer">
  <div class="footer-brand"><span></span>Cedar Crest</div>
  <div class="footer-col" style="left:334px"><h4>Company</h4><ul><li>Home</li><li>About Us</li><li>What We Do</li><li>Why Us</li></ul></div>
  <div class="footer-col" style="left:522px"><h4>Sublinks</h4><ul><li>Our Services</li><li>Our Team</li><li>Testimonials</li><li>Start Trial</li></ul></div>
  <div class="footer-col" style="left:714px;top:60px"><h4>Resources</h4><ul><li>Support</li><li>Clients</li><li>Privacy Policy</li><li>Contact Us</li></ul></div>
  <div class="footer-col" style="left:904px;top:60px"><h4>Follow Us</h4><div class="social"><span></span><span></span><span></span><span></span></div></div>
</footer>
<div class="bottom-bar">© 2017 Company Name &nbsp;All right reserved &nbsp;Term of Use</div>
</body>
</html>
```